Upgrade Wordpress Website

We have an existing website www.bramblefinch.org.au - we require improved shop, improved donation visibility and interactive forms for sponsorship

```html
<!DOCTYPE html>
<html lang="en">
<head>
<meta charset="utf-8">
<title>Bramble Finch Equine Sanctuary</title>
<link href="https://fonts.googleapis.com/css2?family=Cinzel:wght@400;600;700&family=Roboto:wght@400;500;700&display=swap" rel="stylesheet">
<style>
:root{
  --orange:#f5862b;
  --orange-deep:#ee5a24;
  --red:#e23b24;
  --ink:#222;
  --dark:#1b1b1b;
  --black:#0b0b0b;
  --white:#fff;
  --grey:#555;
}
*{box-sizing:border-box;margin:0;padding:0}
html,body{width:1200px;height:5008px;overflow:hidden}
body{font-family:Roboto,Arial,sans-serif;color:var(--ink);background:var(--white)}
section,header,footer,nav{position:relative;width:1200px;overflow:hidden}
.abs{position:absolute}
.btn{position:absolute;display:flex;align-items:center;justify-content:center;border-radius:30px;color:var(--white);
  background:linear-gradient(90deg,var(--orange),var(--orange-deep));font-family:Cinzel,Georgia,serif;font-weight:700;letter-spacing:.5px}
.photo{position:absolute}
.arrow{position:absolute;width:62px;height:62px}
.sec-title{position:absolute;left:0;width:1200px;text-align:center;font-family:Cinzel,Georgia,serif;font-weight:700;font-size:52px;line-height:1}
.underline{display:inline-block;padding-bottom:6px;border-bottom:4px solid currentColor}

/* header */
.site-header{height:117px;background:var(--white)}
.brand{left:117px;top:22px;display:flex;align-items:center;gap:12px}
.brand-name{font-family:Cinzel,Georgia,serif;font-weight:600;color:var(--orange-deep);font-size:26px;line-height:1.05}
.brand-mark{width:50px;height:72px;background:var(--orange)}
.phone{left:668px;top:44px;display:flex;align-items:center;gap:10px;color:var(--orange-deep);font-family:Cinzel,Georgia,serif;font-weight:700;font-size:22px}
.head-donate{left:879px;top:39px;width:171px;height:47px;font-size:16px;background:linear-gradient(90deg,var(--orange-deep),var(--red))}

.main-nav{height:74px;background:var(--orange)}
.main-nav ul{list-style:none;display:flex;gap:21px;position:absolute;left:122px;top:27px}
.main-nav li{font-family:Cinzel,Georgia,serif;font-weight:700;font-size:15px;color:var(--white)}

/* hero */
.hero{height:548px;background:var(--black)}
.hero-photo{left:500px;top:0;width:700px;height:548px;background:radial-gradient(ellipse at 65% 45%,#4a4540 0%,#2a2724 35%,#0b0b0b 70%)}
.hero h1{position:absolute;left:126px;top:100px;color:var(--white);font-family:Cinzel,Georgia,serif;font-weight:700;font-size:58px;line-height:65px;letter-spacing:1px}
.hero .btn{left:126px;top:393px;width:136px;height:47px;font-size:18px}

/* about */
.about{height:498px}
.about-orange{left:120px;top:54px;width:220px;height:397px;background:linear-gradient(180deg,var(--orange),var(--red))}
.about-photo{left:120px;top:54px;width:458px;height:397px;background:linear-gradient(135deg,transparent 30%,rgba(20,20,20,.85) 31%,#111 60%,transparent 85%)}
.about h2{left:648px;top:48px;font-family:Cinzel,Georgia,serif;font-weight:700;font-size:52px;color:var(--orange-deep)}
.about h2 span{border-bottom:3px solid var(--orange-deep);padding-bottom:4px}
.about p{position:absolute;left:648px;top:123px;width:385px;font-size:16px;line-height:27px;color:var(--ink)}
.about .btn{left:646px;top:405px;width:157px;height:42px;font-size:17px}

/* shop */
.shop{height:640px;background:radial-gradient(ellipse at 50% 40%,#2e2e2e,var(--dark) 70%)}
.shop .sec-title{top:63px;color:var(--white)}
.shop-intro{position:absolute;left:210px;width:780px;top:146px;text-align:center;color:var(--white);font-size:17px;line-height:27px}
.product{position:absolute;top:237px;width:224px;height:331px;background:var(--white);text-align:center}
.product .img{height:171px}
.product h3{font-family:Cinzel,Georgia,serif;color:var(--orange-deep);font-weight:600;font-size:15px;line-height:23px;margin-top:22px}
.product .price{font-family:Cinzel,Georgia,serif;font-weight:700;font-size:16px;margin-top:10px}
.product .btn{left:67px;top:275px;width:90px;height:30px;font-size:10px}

/* sponsorship */
.sponsor{height:755px}
.sponsor .sec-title{top:66px;color:var(--orange-deep)}
.sponsor-intro{position:absolute;left:190px;width:820px;top:144px;text-align:center;font-size:17px;line-height:27px}
.animal{position:absolute;top:249px;width:450px;text-align:center}
.animal .img{height:231px;box-shadow:0 6px 14px rgba(0,0,0,.2)}
.animal h3{font-family:Cinzel,Georgia,serif;color:var(--orange-deep);font-weight:700;font-size:22px;margin-top:24px}
.animal p{font-size:14px;line-height:22px;margin:10px 10px 0}
.animal .btn{position:relative;margin:20px auto 0;width:157px;height:42px;font-size:17px}

/* news */
.news{height:655px;background:var(--orange)}
.news .sec-title{top:48px;color:var(--white)}
.post{position:absolute;top:171px;width:296px;height:406px;background:var(--white);border-radius:90px 0 60px 60px;overflow:hidden;text-align:center}
.post .img{height:187px}
.post h3{font-family:Cinzel,Georgia,serif;font-weight:700;font-size:17px;line-height:26px;margin-top:18px}
.post p{font-size:12px;line-height:17px;margin:8px 22px 0;color:var(--grey)}
.post .btn{left:88px;top:350px;width:118px;height:30px;font-size:12px}

/* media */
.media{height:632px}
.media .sec-title{top:62px;color:var(--orange-deep)}
.media-photo{left:0;top:185px;width:696px;height:379px;border-radius:0 190px 190px 0;background:linear-gradient(120deg,#6d5a3e,#8a7a5c 45%,#4f6b3a)}
.play{left:250px;top:304px;width:88px;height:88px;border-radius:50%;background:var(--orange-deep);display:flex;align-items:center;justify-content:center}
.play i{width:22px;height:22px;background:var(--white)}
.media p{position:absolute;left:733px;top:283px;width:300px;font-size:17px;line-height:22px}

/* donate */
.donate{height:594px;background:linear-gradient(180deg,var(--orange) 0%,var(--orange-deep) 60%,var(--red) 100%);color:var(--white);text-align:center}
.donate-art{top:175px;width:240px;height:419px;background:linear-gradient(180deg,rgba(0,0,0,0),rgba(0,0,0,.3))}
.donate h2{position:absolute;left:0;width:1200px;top:56px;font-family:Cinzel,Georgia,serif;font-weight:700;font-size:46px;line-height:50px}
.donate h2 small{display:block;font-size:34px;line-height:46px}
.donate .note{position:absolute;left:0;width:1200px;top:186px;font-weight:700;font-size:20px;line-height:27px}
.donate .amount{position:absolute;left:0;width:1200px;top:250px;font-weight:700;font-size:44px}
.donate .monthly{position:absolute;left:0;width:1200px;top:318px;font-size:16px;display:flex;justify-content:center;align-items:center;gap:8px}
.donate .monthly i{width:14px;height:14px;background:var(--white);border-radius:2px}
.pay{position:absolute;left:364px;width:472px;height:51px;background:var(--white);color:var(--ink);border-radius:30px;display:flex;align-items:center;justify-content:center;font-size:17px}
.pay.cta{color:var(--orange-deep);font-family:Cinzel,Georgia,serif;font-weight:700;font-size:20px}

/* footer */
.site-footer{height:427px;background:radial-gradient(ellipse at 30% 40%,#2a2a2a,var(--black) 70%);color:var(--white)}
.site-footer h4{font-family:Cinzel,Georgia,serif;font-weight:700;font-size:27px;position:absolute;top:68px}
.contact-list{position:absolute;left:136px;top:116px;font-size:17px;line-height:27px}
.contact-list .row{display:flex;gap:12px;margin-bottom:12px}
.contact-list svg{flex:none;margin-top:4px}
.links{position:absolute;left:519px;top:125px;list-style:none;font-size:13px;line-height:22.5px;font-weight:500}
.bank{position:absolute;left:751px;top:113px;font-size:14px;line-height:26px}
.bank .acct{font-family:Cinzel,Georgia,serif;font-size:16px;margin-top:6px}
.email{position:absolute;left:747px;top:247px;width:249px;height:50px;background:var(--white);border-radius:25px;color:var(--grey);font-size:11px;display:flex;align-items:center;padding-left:16px}
.site-footer .btn{left:747px;top:315px;width:249px;height:48px;font-size:18px}
.copyright{height:68px;background:linear-gradient(90deg,var(--orange-deep),var(--red));color:var(--white);font-size:13px;display:flex;align-items:center;justify-content:center}
</style>
</head>
<body>

<header class="site-header">
  <div class="abs brand">
    <div class="brand-name">Bramble<br>Finch</div>
    <div class="brand-mark"></div>
  </div>
  <div class="abs phone">
    <svg width="22" height="22" viewBox="0 0 24 24"><path d="M6.6 10.8a15 15 0 006.6 6.6l2.2-2.2a1 1 0 011-.25 11.4 11.4 0 003.6.57 1 1 0 011 1V20a1 1 0 01-1 1A17 17 0 013 4a1 1 0 011-1h3.5a1 1 0 011 1c0 1.25.2 2.45.57 3.57a1 1 0 01-.25 1z" fill="none" stroke="#ee5a24" stroke-width="2"/></svg>
    0400 555 182
  </div>
  <div class="btn head-donate">DONATE NOW</div>
</header>

<nav class="main-nav">
  <ul>
    <li>HOME</li><li>FOR ADOPTION</li><li>FOR SPONSORSHIP</li><li>SHOP</li><li>LEASE</li><li>ADOPTED</li><li>SPONSERED</li><li>R.I.P</li><li>CONTACT &amp; FORMS</li>
  </ul>
</nav>

<section class="hero">
  <div class="photo hero-photo" role="img" aria-label="Dark horse head with flowing mane on black background"></div>
  <h1>BRAMBLE<br>FINCH<br>EQUINE<br>SANCTUARY</h1>
  <div class="btn">DONATE</div>
</section>

<section class="about">
  <div class="photo about-orange"></div>
  <div class="photo about-photo" role="img" aria-label="Black horse rearing in front of an orange panel"></div>
  <h2 class="abs"><span>ABOUT US</span></h2>
  <p>Bramble Finch Equine Sanctuary (BFES) was founded by passionate animal lovers and advocates in 2014, in response to an ever-increasing number of horses passing through the saleyards, and into the hands of knackeries.The name was selected to pay homage to the brilliant protective work done by the Ocean Guardians, and to reflect our mission of providing sanctuary and solace to unwanted, injured, and otherwise vulnerable horses</p>
  <div class="btn">READ MORE</div>
</section>

<section class="shop">
  <h2 class="sec-title"><span class="underline">OUR SHOP</span></h2>
  <p class="shop-intro">Our shop allows you to purchase our Bramble Finch Equine Sanctuary merchandise (coming soon), as well as being able to make donations towards our every day costs.</p>
  <svg class="arrow" style="left:22px;top:366px" viewBox="0 0 62 62"><circle cx="31" cy="31" r="29" fill="none" stroke="#ee5a24" stroke-width="3"/><path d="M44 27H28v-7L15 31l13 11v-7h16z" fill="none" stroke="#f5862b" stroke-width="3" stroke-linejoin="round"/></svg>
  <svg class="arrow" style="left:1116px;top:366px" viewBox="0 0 62 62"><circle cx="31" cy="31" r="29" fill="none" stroke="#ee5a24" stroke-width="3"/><path d="M18 27h16v-7l13 11-13 11v-7H18z" fill="none" stroke="#f5862b" stroke-width="3" stroke-linejoin="round"/></svg>
  <div class="product" style="left:107px"><div class="img" role="img" aria-label="Candle product photo with grey horses" style="background:linear-gradient(135deg,#c9c4b8,#8d8a7f 60%,#b9733a)"></div><h3>CANDLES POURED<br>WITH LOVE</h3><div class="price">$24.00</div><div class="btn">SHOP NOW</div></div>
  <div class="product" style="left:358px"><div class="img" role="img" aria-label="Candle product photo with horses and a cart" style="background:linear-gradient(135deg,#9aa08a,#5d6a48 55%,#7a3a24)"></div><h3>CANDLES POURED<br>WITH LOVE</h3><div class="price">$24.00</div><div class="btn">SHOP NOW</div></div>
  <div class="product" style="left:607px"><div class="img" role="img" aria-label="Candle product photo with horses running by trees" style="background:linear-gradient(135deg,#a8b6c0,#4c5d3c 55%,#5b3a26)"></div><h3>CANDLES POURED<br>WITH LOVE</h3><div class="price">$24.00</div><div class="btn">SHOP NOW</div></div>
  <div class="product" style="left:856px"><div class="img" role="img" aria-label="Candle product photo with three horses" style="background:linear-gradient(135deg,#b7a98c,#8c5a32 55%,#2f2a24)"></div><h3>CANDLES POURED<br>WITH LOVE</h3><div class="price">$24.00</div><div class="btn">SHOP NOW</div></div>
</section>

<section class="sponsor">
  <h2 class="sec-title"><span class="underline">FOR SPONSORSHIP</span></h2>
  <p class="sponsor-intro">At The Bramble Finch Equine Sanctuary, we have a number of our animals available for Sponsorship. The majority are horses or ponies reflecting our focus however from time to time the odd farm animal finds itself needing the peace of our Sanctuary.</p>
  <svg class="arrow" style="left:27px;top:370px" viewBox="0 0 62 62"><circle cx="31" cy="31" r="29" fill="none" stroke="#ee5a24" stroke-width="3"/><path d="M44 27H28v-7L15 31l13 11v-7h16z" fill="none" stroke="#f5862b" stroke-width="3" stroke-linejoin="round"/></svg>
  <svg class="arrow" style="left:1097px;top:370px" viewBox="0 0 62 62"><circle cx="31" cy="31" r="29" fill="none" stroke="#ee5a24" stroke-width="3"/><path d="M18 27h16v-7l13 11-13 11v-7H18z" fill="none" stroke="#f5862b" stroke-width="3" stroke-linejoin="round"/></svg>
  <div class="animal" style="left:130px">
    <div class="img" role="img" aria-label="White pony standing in a paddock" style="background:linear-gradient(135deg,#7c8a6a,#e8e6df 45%,#6b7458)"></div>
    <h3>SHIMMER</h3>
    <p>Beautiful little Shimmer is a very aged pony. We place him at over 30 at least – slowly putting on weight after treatment for an unusual infection – he now has the pleasure of roaming the Sanctuary – making friends and clearing the sweet grass spots. Often spotted laying in the sun beside Bella and</p>
    <div class="btn">READ MORE</div>
  </div>
  <div class="animal" style="left:595px">
    <div class="img" role="img" aria-label="Brown pony on a lead in a paddock" style="background:linear-gradient(135deg,#8a7f56,#7a4a2c 50%,#9a9468)"></div>
    <h3>SPUD</h3>
    <p>Such a cool dude BFES Spud was purchased via online sales for just $75 and then surrendered to Bramble Finch to be gelded and managed. We have discovered that he loves girls – no surprise and the Gold Rush Trail. Spud has a large scar from a fight with a horse stallion</p>
    <div class="btn">READ MORE</div>
  </div>
</section>

<section class="news">
  <h2 class="sec-title"><span class="underline">LATEST NEWS</span></h2>
  <svg class="arrow" style="left:27px;top:299px" viewBox="0 0 62 62"><circle cx="31" cy="31" r="29" fill="none" stroke="#fff" stroke-width="3"/><path d="M44 27H28v-7L15 31l13 11v-7h16z" fill="none" stroke="#fff" stroke-width="3" stroke-linejoin="round"/></svg>
  <svg class="arrow" style="left:1100px;top:299px" viewBox="0 0 62 62"><circle cx="31" cy="31" r="29" fill="none" stroke="#fff" stroke-width="3"/><path d="M18 27h16v-7l13 11-13 11v-7H18z" fill="none" stroke="#fff" stroke-width="3" stroke-linejoin="round"/></svg>
  <div class="post" style="left:134px"><div class="img" role="img" aria-label="Horses in rugs under a large tree" style="background:linear-gradient(135deg,#9c9a82,#5a5470 50%,#6b7a4a)"></div><h3>148 Years of Horse<br>August 12, 2020</h3><p>BFES 148 years of horse in this photo! If only they could talk to us.... Gentle eyes that have seen so much Velvet muzzles that are so soft to touch</p><div class="btn">READ MORE</div></div>
  <div class="post" style="left:447px"><div class="img" role="img" aria-label="Chestnut horse grazing, video still" style="background:linear-gradient(135deg,#6f7a52,#8a4a28 50%,#3a3a30)"></div><h3>Nurse BFES Bob<br>August 12, 2020</h3><p>Sed ut perspiciatis unde omnis iste natus error sit voluptatem accusantium doloremque laudantium, totam rem aperiam, a sunt explicabo.</p><div class="btn">READ MORE</div></div>
  <div class="post" style="left:757px"><div class="img" role="img" aria-label="Horse at a feed shed" style="background:linear-gradient(135deg,#5a6e8a,#7a4a3a 50%,#8a6a4a)"></div><h3>BFES Norman 35 yrs<br>young August 12, 2020</h3><p>Woohoo BFES Norman is our oldest resident at 35 years of age and today after his weigh-in he was given a 5 minute treat to help himself in the feed shed.</p><div class="btn">READ MORE</div></div>
</section>

<section class="media">
  <h2 class="sec-title"><span class="underline">MEDIA</span></h2>
  <div class="photo media-photo" role="img" aria-label="Video still of a sanctuary carer outdoors with a dog"></div>
  <div class="abs play"><i></i></div>
  <p>Each horse will always have its own specific needs addressed and for us, there is no rush. Taking time to learn more about each horse allows us to better assess them for adoption suitability. We take the worry out of purchasing an ‘unknown’ horse for you</p>
</section>

<section class="donate">
  <div class="abs donate-art" style="left:0" role="img" aria-label="Black rearing horse silhouette"></div>
  <div class="abs donate-art" style="right:0" role="img" aria-label="Black rearing horse silhouette"></div>
  <h2>DONATE TO<small>Bramble Finch Equine Sanctuary</small></h2>
  <p class="note">We are a deductible gift receipient -All donations<br>over $2 are tax deductible</p>
  <div class="amount">$ 0.00 AUD</div>
  <div class="monthly"><i></i>Make this a monthly donation</div>
  <div class="pay" style="top:372px">Donate with e-wallet</div>
  <div class="pay" style="top:444px">Donate with credit or debit card</div>
  <div class="pay cta" style="top:510px">DONATE NOW</div>
</section>

<footer class="site-footer">
  <h4 style="left:136px">CONTACT US</h4>
  <div class="contact-list">
    <div class="row"><svg width="20" height="24" viewBox="0 0 20 24"><path d="M10 1a8 8 0 00-8 8c0 6 8 14 8 14s8-8 8-14a8 8 0 00-8-8z" fill="#f5862b"/><circle cx="10" cy="9" r="3" fill="#111"/></svg><div>Bramble Finch Equine<br>Sanctuary<br>Ashvale VIC 3999</div></div>
    <div class="row"><svg width="20" height="20" viewBox="0 0 24 24"><path d="M6.6 10.8a15 15 0 006.6 6.6l2.2-2.2a1 1 0 011-.25 11.4 11.4 0 003.6.57 1 1 0 011 1V20a1 1 0 01-1 1A17 17 0 013 4a1 1 0 011-1h3.5a1 1 0 011 1c0 1.25.2 2.45.57 3.57a1 1 0 01-.25 1z" fill="#f5862b"/></svg><div>0400 555 182<br>0400 555 907</div></div>
    <div class="row"><svg width="20" height="16" viewBox="0 0 20 16"><rect x="1" y="1" width="18" height="14" fill="#f5862b"/><path d="M1 1l9 8 9-8" fill="none" stroke="#111" stroke-width="1.5"/></svg><div>admin@bramblefinch.org.au</div></div>
  </div>
  <h4 style="left:519px">LINKS</h4>
  <ul class="links">
    <li>HOME</li><li>FOR ADOPTION</li><li>FOR SPONSORSHIP</li><li>SHOP</li><li>LEASE</li><li>ADOPTED</li><li>SPONSERED</li><li>R.I.P</li><li>CONTACT &amp; FORMS</li>
  </ul>
  <h4 style="left:751px">DONATE</h4>
  <div class="bank">Southern Bank Account: Bramble Finch<br>Equine Sanctuary<br>BSB: 000 111<div class="acct">ACCOUNT: 100200300</div></div>
  <div class="email">YOUR EMAIL ADDRESS</div>
  <div class="btn">SUBSCRIBE</div>
</footer>

<div class="copyright">2022 © ALL RIGHTS RESERVED BRAMBLE FINCH ENQUINE SANCTUARY</div>

</body>
</html>
```